Snowplowing Flyer - 8.5x11, one sided

We are looking to redesign our flyer for winter snowplowing to match our other collateral material. I have attached a few files to show what our new marketing material looks like and we are looking to have a new flyer done that is: (1) 8.5"x11" (one sided); (2) CMYK for printing; and (3) minimum 300 dpi suitable for printing.

We would like color photo(s) of snowplowing trucks (at least one) and it should have the following text on it...

Our logo and contact information (just street/email/web/phone number)

Plowing whenever 1" of accumulated snow has fallen, normally by 6am depending upon time and amount

Plowing multiple times per 24 hour period during heavy snowfalls

A fleet of 20 plow trucks w multiple backup plow trucks to ensure our performance

Email based plowing information with real time updates for clients

Double driveways starting at $238, triple driveways starting at $258

Hand shoveling of front walkways and porches available

Salting of driveways available

Fully licensed and insured for your protection

Please contact us by phone or email to request a proposal.

Target Market(s)

Residential homeowners.

Industry/Entity Type

Snow Removal

Font styles to use
Sans Serif

Colors

Designer to choose colors to be used in the design.

Requirements
Must have
• A similar feel to the rest of our marketing material which I have attached. Should be easy to read and fun to look at.
Nice to have
• A photo of a snowplow truck similar to the one in our existing material and on our website.
Should not have
• Should not be cluttered. Should keep a similar color scheme to the rest of our marketing material.

```html
<!DOCTYPE html>
<html lang="en">
<head>
<meta charset="utf-8">
<title>Willow Ridge Landscaping – Snow Plowing Flyer</title>
<link href="https://fonts.googleapis.com/css2?family=Lato:wght@400;700;900&display=swap" rel="stylesheet">
<style>
  :root{
    --backdrop:#1b1d20;
    --sheet:#151617;
    --green:#2fb45f;
    --green-dark:#1f8f47;
    --ink:#111213;
    --white:#f4f5f5;
    --muted:#d9dcdc;
    --sky:#5ea3e0;
    --rule:#cfd2d2;
  }
  *{margin:0;padding:0;box-sizing:border-box}
  html,body{width:1200px;height:848px;overflow:hidden;background:var(--backdrop)}
  body{font-family:'Lato',sans-serif;color:var(--white)}
  .flyer{position:absolute;left:288px;top:20px;width:624px;height:808px;background:var(--sheet);overflow:hidden}
  .hero{position:absolute;left:0;top:0;width:624px;height:420px}
  .brand{position:absolute;top:362px;left:0;width:624px;text-align:center}
  .brand-name{font-size:30px;font-weight:400;letter-spacing:9px;text-transform:uppercase;color:var(--white)}
  .brand-sub{font-size:11px;font-weight:400;letter-spacing:10px;text-transform:uppercase;color:var(--white);margin-top:4px}
  .services{position:absolute;left:44px;top:462px;width:536px;height:238px;border:3px solid var(--green);border-radius:20px}
  .headline{position:absolute;left:90px;top:436px;width:444px;background:var(--green);border-radius:22px;padding:10px 18px;text-align:center;color:var(--ink);font-weight:900;font-size:17px;line-height:1.2}
  .columns{position:absolute;left:16px;right:16px;top:70px;display:flex;gap:26px}
  .column{flex:1;list-style:none}
  .column li{position:relative;padding-left:12px;font-size:12.5px;line-height:1.3;padding-bottom:7px;margin-bottom:7px;border-bottom:1px solid var(--rule)}
  .column li:last-child{border-bottom:none;margin-bottom:0;padding-bottom:0}
  .column li.plain{border-bottom:none;margin-bottom:0;padding-bottom:3px}
  .column li::before{content:"";position:absolute;left:0;top:4px;border-left:6px solid var(--green);border-top:4px solid transparent;border-bottom:4px solid transparent}
  .cta{position:absolute;left:90px;top:712px;width:444px;height:34px;line-height:34px;background:var(--green);border-radius:17px;text-align:center;font-size:15px;font-weight:700;color:var(--white)}
  .contact{position:absolute;left:0;top:754px;width:624px;text-align:center;font-size:13px;line-height:1.6;font-style:normal}
  .contact svg{width:11px;height:11px;vertical-align:-1px;margin-right:4px}
  .contact .gap{display:inline-block;width:12px}
</style>
</head>
<body>
<main class="flyer">
  <svg class="hero" viewBox="0 0 624 420" xmlns="http://www.w3.org/2000/svg">
    <defs>
      <linearGradient id="snowScene" x1="0" y1="0" x2="1" y2="1">
        <stop offset="0" stop-color="#f2f3f4"/><stop offset=".55" stop-color="#c4c8cb"/><stop offset="1" stop-color="#eceeef"/>
      </linearGradient>
      <radialGradient id="spreaderTone"><stop offset="0" stop-color="#8a6a52"/><stop offset="1" stop-color="#c9c2b8"/></radialGradient>
      <radialGradient id="shovelTone"><stop offset="0" stop-color="#e6e8ea"/><stop offset=".6" stop-color="#d65a5a"/><stop offset="1" stop-color="#9a8370"/></radialGradient>
      <radialGradient id="loaderTone"><stop offset="0" stop-color="#e08b3a"/><stop offset="1" stop-color="#e9ecee"/></radialGradient>
    </defs>
    <path d="M0 0H624V350C470 330 300 300 0 235Z" fill="url(#snowScene)" role="img" aria-label="Photo of a pickup truck with a snow plow clearing a snowy driveway"/>
    <path d="M0 235C300 300 470 330 624 350" fill="none" stroke="var(--sky)" stroke-width="6"/>
    <g stroke="var(--sky)" stroke-width="3">
      <circle cx="92" cy="232" r="64" fill="url(#spreaderTone)" role="img" aria-label="Photo of a salt spreader scattering salt on the road"/>
      <circle cx="318" cy="296" r="58" fill="url(#shovelTone)" role="img" aria-label="Photo of a red shovel lifting snow"/>
      <circle cx="540" cy="336" r="58" fill="url(#loaderTone)" role="img" aria-label="Photo of a loader clearing snow"/>
    </g>
  </svg>

  <div class="brand">
    <div class="brand-name">Willow Ridge</div>
    <div class="brand-sub">Landscaping</div>
  </div>

  <section class="services">
    <div class="columns">
      <ul class="column">
        <li>Plowing multiple times per 24 hour period during heavy snowfalls</li>
        <li>A fleet of 20 plow trucks w multiple backup plow trucks to ensure our performance</li>
        <li>Email based plowing information with real time updates for clients</li>
      </ul>
      <ul class="column">
        <li>Double driveways starting at $238, triple driveways starting at $258</li>
        <li class="plain">Hand shoveling of front walkways and porches available</li>
        <li class="plain">Salting of driveways available</li>
        <li>Fully licensed and insured for your protection</li>
      </ul>
    </div>
  </section>
  <h1 class="headline">Plowing Whenever 1" Of Accumulated Snow Has Fallen, Normally By 6am Depending Upon Time And Amount</h1>

  <p class="cta">Please contact us by phone or email to request a proposal.</p>

  <address class="contact">
    <div><svg viewBox="0 0 12 12"><circle cx="6" cy="6" r="5.5" fill="var(--green)"/><path d="M6 2.5a2 2 0 0 0-2 2c0 1.6 2 4 2 4s2-2.4 2-4a2 2 0 0 0-2-2z" fill="var(--sheet)"/></svg>1480 Maple Hollow Road NE, Cedar Falls, MI 49301</div>
    <div><svg viewBox="0 0 12 12"><circle cx="6" cy="6" r="5.5" fill="var(--green)"/><path d="M4 3l1.2 1.4-.6.9a4 4 0 0 0 2.1 2.1l.9-.6L9 8 8 9C5.5 8.6 3.4 6.5 3 4z" fill="var(--sheet)"/></svg>(555) 214-7730<span class="gap"></span><svg viewBox="0 0 12 12"><circle cx="6" cy="6" r="5.5" fill="var(--green)"/><rect x="3" y="4" width="6" height="4.2" fill="var(--sheet)"/><path d="M3 4l3 2.3L9 4" fill="none" stroke="var(--green)" stroke-width=".8"/></svg>hello@willowridgeyard.com</div>
  </address>
</main>
</body>
</html>
```